Criação de Papelaria Profissional para Contabilidade & Finanças
" ESTOU INICANDO AGORA O ESCRITORIO DE CONTABILIDADE, QUERO ATUAR NO RAMO DE TREINAMENTO ATRAVÉS DO COACHING , FAZER CONSULTORIAS NA AREA CONTABIL, SERVIÇOS CONTABEIS EM GERAL, DESDE O MICROEMPREENDEDOR ATÉ O A EMPRESA DE GRANDE PORTE LUCRO REAL "

```html
<!DOCTYPE html>
<html lang="pt-BR">
<head>
<meta charset="UTF-8">
<title>VQS Consultoria Contábil &amp; Fiscal — Papelaria</title>
<link href="https://fonts.googleapis.com/css2?family=Montserrat:wght@400;600;700&display=swap" rel="stylesheet">
<style>
  :root {
    --page-bg: #ececee;
    --navy-deep: #03061a;
    --navy-mid: #0a1550;
    --navy-bright: #1a2f9a;
    --gold: #d9a93a;
    --gold-light: #f2d27a;
    --paper: #f7f7f8;
    --paper-shade: #e2e3e6;
    --ink-gray: #6b6e76;
  }
  * { margin: 0; padding: 0; box-sizing: border-box; }
  html, body { width: 1200px; height: 1200px; overflow: hidden; }
  body {
    background: var(--page-bg);
    font-family: "Montserrat", sans-serif;
    display: flex;
    align-items: center;
    justify-content: center;
    gap: 60px;
  }
  .folder {
    position: relative;
    width: 520px;
    height: 740px;
    overflow: hidden;
    box-shadow: 0 8px 24px rgba(0,0,0,0.18);
  }

  /* Dark cover */
  .folder--cover {
    background: linear-gradient(100deg, var(--navy-deep) 0%, var(--navy-mid) 45%, var(--navy-deep) 100%);
  }
  .folder--cover .chevron-strip {
    position: absolute; left: 0; top: 0;
    width: 320px; height: 640px;
    background: linear-gradient(90deg, rgba(26,47,154,0.55) 0%, rgba(26,47,154,0.25) 60%, rgba(26,47,154,0) 100%);
  }
  .cover-brand {
    position: absolute; left: 48px; top: 270px;
  }
  .cover-brand .brand-name {
    font-weight: 700;
    font-size: 96px;
    letter-spacing: 2px;
    line-height: 1;
    color: var(--gold);
  }
  .cover-brand .brand-tagline {
    margin-top: 10px;
    font-weight: 600;
    font-size: 15px;
    letter-spacing: 1.5px;
    color: var(--gold);
  }
  .folder--cover .gold-rule {
    position: absolute; left: 0; right: 0; bottom: 56px;
    height: 2px;
    background: linear-gradient(90deg, transparent, var(--gold-light) 30%, var(--gold) 70%, transparent);
  }

  /* Light letterhead */
  .folder--letterhead {
    background: linear-gradient(90deg, var(--paper-shade) 0%, var(--paper) 40%, #ffffff 100%);
  }
  .folder--letterhead .chevron-strip {
    position: absolute; left: 0; top: 0;
    width: 300px; height: 560px;
    background: linear-gradient(90deg, rgba(180,182,188,0.55) 0%, rgba(210,212,216,0.3) 60%, rgba(255,255,255,0) 100%);
  }
  .letterhead-brand {
    position: absolute; left: 0; right: 0; top: 600px;
    text-align: center;
  }
  .letterhead-brand .brand-name {
    font-weight: 700;
    font-size: 38px;
    letter-spacing: 1px;
    line-height: 1;
    color: var(--navy-deep);
  }
  .letterhead-brand .brand-tagline {
    margin-top: 4px;
    font-weight: 600;
    font-size: 7px;
    letter-spacing: 1px;
    color: var(--navy-deep);
  }
  .contact-row {
    position: absolute; left: 40px; right: 40px; bottom: 30px;
    display: flex; justify-content: space-between;
  }
  .contact-item {
    display: flex; align-items: center; gap: 6px;
    font-size: 7px; line-height: 1.4;
    color: var(--ink-gray);
  }
  .contact-item svg { width: 12px; height: 12px; flex: none; }
  .folder--letterhead .gold-rule {
    position: absolute; left: 0; right: 0; bottom: 14px;
    height: 2px;
    background: linear-gradient(90deg, transparent, var(--gold) 30%, var(--gold-light) 70%, transparent);
  }
</style>
</head>
<body>

  <section class="folder folder--cover">
    <div class="chevron-strip" role="img" aria-label="Faixa decorativa de chevrons empilhados em azul"></div>
    <div class="cover-brand">
      <div class="brand-name">VQS</div>
      <div class="brand-tagline">CONSULTORIA CONTÁBIL &amp; FISCAL</div>
    </div>
    <div class="gold-rule"></div>
  </section>

  <section class="folder folder--letterhead">
    <div class="chevron-strip" role="img" aria-label="Faixa decorativa de chevrons empilhados em cinza claro"></div>
    <div class="letterhead-brand">
      <div class="brand-name">VQS</div>
      <div class="brand-tagline">CONSULTORIA CONTÁBIL &amp; FISCAL</div>
    </div>
    <div class="contact-row">
      <div class="contact-item">
        <svg viewBox="0 0 12 12"><circle cx="6" cy="6" r="5.5" fill="none" stroke="#6b6e76"/><path d="M4 3.5 L5 3.5 L5.5 5 L4.8 5.5 Q5.5 7 6.5 7.2 L7 6.5 L8.5 7 L8.5 8 Q5 8.5 4 3.5Z" fill="#6b6e76"/></svg>
        <span>(11) 4000-2100<br>(11) 98800-4321</span>
      </div>
      <div class="contact-item">
        <svg viewBox="0 0 12 12"><circle cx="6" cy="6" r="5.5" fill="none" stroke="#6b6e76"/><path d="M6 2.8 A2 2 0 0 1 8 4.8 Q8 6.5 6 9 Q4 6.5 4 4.8 A2 2 0 0 1 6 2.8Z" fill="#6b6e76"/></svg>
        <span>Rua das Acácias, 250<br>Centro - São Paulo/SP</span>
      </div>
      <div class="contact-item">
        <svg viewBox="0 0 12 12"><circle cx="6" cy="6" r="5.5" fill="none" stroke="#6b6e76"/><rect x="3" y="4" width="6" height="4" fill="none" stroke="#6b6e76" stroke-width="0.8"/><path d="M3 4 L6 6.3 L9 4" fill="none" stroke="#6b6e76" stroke-width="0.8"/></svg>
        <span>contato@vqsconsult.com.br<br>www.vqsconsult.com.br</span>
      </div>
    </div>
    <div class="gold-rule"></div>
  </section>

</body>
</html>
```